Stonebell Inc Ad Design, trying to attract new customers

Please see attached pictures and files for information
We are a Class A - Residential General Contractor in Lynchburg, VA with Master HVAC and Master PLUMBING Licenses. We focus on Water and Air Solutions for property owners.
We build, remodel, and repair homes
We do HVAC, including Humidity Control and Air Purification
We do Plumbing
We love to fix Water Leaks for Plumbing, Roof Leaks, Skylight Leaks, Basement Leaks, Foundation Leaks, Door and Window Leaks
We solve water and air issues on the outside of properties with custom structures, grading, and landscaping

Target Market(s)

Residential and Light Commercial property owners

Industry/Entity Type

Construction

Font styles to use
Other font styles liked:
• see cards

Colors
0054AA
0677BA
7BADD7
CADEEF
E8F1F8
00AB8E
00BBA5
67D7C9
C6EFE9
E9F9F6

Requirements
Must have
• See business cards
Nice to have
• see business cards
Should not have
• My name

```html
<!DOCTYPE html>
<html lang="en">
<head>
<meta charset="utf-8">
<title>Stonebell Inc Billboard</title>
<link href="https://fonts.googleapis.com/css2?family=Anton&family=Montserrat:wght@500;600;700;800&display=swap" rel="stylesheet">
<style>
  :root {
    --page-bg: #2e2e2e;
    --white: #ffffff;
    --green-dark: #0b6e35;
    --green-mid: #1a8a3e;
    --green-light: #3cb54a;
    --sky-blue: #0a9be0;
    --brand-blue: #1a6fc0;
  }
  * { margin: 0; padding: 0; box-sizing: border-box; }
  html, body {
    width: 1085px;
    height: 1200px;
    overflow: hidden;
    background: var(--page-bg);
  }
  .billboard-frame {
    position: absolute;
    left: 30px;
    top: 366px;
    width: 1025px;
    height: 468px;
    box-shadow: 0 18px 40px rgba(0,0,0,0.55);
  }
  .billboard {
    position: absolute;
    left: 0;
    top: 0;
    width: 1512px;
    height: 690px;
    transform: scale(0.6779);
    transform-origin: top left;
    background: var(--white);
    overflow: hidden;
  }
  .billboard-waves {
    position: absolute;
    inset: 0;
  }
  .brand {
    position: absolute;
    left: 0;
    right: 0;
    top: 100px;
    display: flex;
    justify-content: center;
    align-items: center;
    gap: 22px;
  }
  .brand-dot {
    width: 46px;
    height: 46px;
    border-radius: 50%;
    background: var(--green-light);
  }
  .brand-name {
    font-family: "Montserrat", sans-serif;
    font-weight: 800;
    font-size: 66px;
    letter-spacing: 2px;
    color: var(--brand-blue);
    text-transform: uppercase;
  }
  .headline {
    position: absolute;
    left: 0;
    right: 0;
    top: 293px;
    text-align: center;
    font-family: "Anton", sans-serif;
    font-size: 92px;
    line-height: 1;
    color: var(--white);
    letter-spacing: 0.5px;
  }
  .credentials {
    position: absolute;
    left: 0;
    right: 0;
    top: 396px;
    text-align: center;
    font-family: "Montserrat", sans-serif;
    font-weight: 800;
    font-size: 52px;
    line-height: 1;
    color: var(--white);
  }
  .license-pill {
    position: absolute;
    left: 466px;
    top: 478px;
    width: 580px;
    height: 88px;
    border: 6px solid var(--white);
    border-radius: 44px;
    background: var(--sky-blue);
    display: flex;
    align-items: center;
    justify-content: center;
    font-family: "Montserrat", sans-serif;
    font-weight: 600;
    font-size: 44px;
    letter-spacing: 2px;
    color: var(--white);
  }
  .contact-line {
    position: absolute;
    left: 0;
    right: 0;
    top: 585px;
    height: 75px;
    display: flex;
    align-items: center;
    justify-content: center;
    color: var(--white);
  }
  .phone-icon {
    width: 60px;
    height: 60px;
    margin-right: 18px;
  }
  .phone-number {
    font-family: "Anton", sans-serif;
    font-size: 72px;
    letter-spacing: 1px;
    line-height: 1;
  }
  .divider {
    width: 6px;
    height: 62px;
    background: var(--white);
    margin: 0 34px;
  }
  .web-address {
    font-family: "Montserrat", sans-serif;
    font-weight: 500;
    font-size: 58px;
    letter-spacing: 2px;
    line-height: 1;
  }
</style>
</head>
<body>
  <div class="billboard-frame">
    <div class="billboard">
      <svg class="billboard-waves" viewBox="0 0 1512 690" width="1512" height="690" aria-hidden="true">
        <defs>
          <linearGradient id="greenField" x1="0" y1="0" x2="1" y2="0">
            <stop offset="0" stop-color="#15803a"/>
            <stop offset="0.5" stop-color="#3cb54a"/>
            <stop offset="1" stop-color="#0b6e35"/>
          </linearGradient>
        </defs>
        <path d="M0,138 C250,100 460,235 760,258 C1060,282 1350,130 1512,30 L1512,548 C1250,522 950,512 760,513 C520,515 220,530 0,546 Z" fill="url(#greenField)"/>
        <path d="M0,570 C260,552 520,538 760,538 C1010,538 1290,552 1512,582 L1512,690 L0,690 Z" fill="#0a9be0"/>
      </svg>

      <div class="brand">
        <span class="brand-dot"></span>
        <span class="brand-name">Stonebell Inc</span>
      </div>

      <h1 class="headline">WE PUT WATER AND&nbsp; AIR IN ITS PLACE</h1>
      <p class="credentials">CLASS A RBC PLUMBING HVAC</p>

      <div class="license-pill">Licensed and Insured</div>

      <div class="contact-line">
        <svg class="phone-icon" viewBox="0 0 60 60" aria-hidden="true">
          <circle cx="30" cy="30" r="28" fill="#ffffff"/>
          <path d="M21 15c2-1 4 0 5 2l3 6c1 2 0 3-1 4l-2 2c1 4 4 7 8 9l2-2c1-1 3-2 4-1l6 3c2 1 3 3 2 5l-2 3c-2 2-5 2-8 1-9-3-16-10-19-19-1-3-1-6 1-8z" fill="#0a9be0"/>
        </svg>
        <span class="phone-number">434-555-0182</span>
        <span class="divider"></span>
        <span class="web-address">StonebellHomesVA.com</span>
      </div>
    </div>
  </div>
</body>
</html>
```